Trifold - Gentle Horizon Therapy

Marianne Dobbs, Psy.D.Licensed Psychologist

this is for hypnosis and meditation
I like decorative font for my name (conservative decorative)

calming effect is most imortant

Target Market(s)

clients with depression, pain, anxiety - adults and aged

Industry/Entity Type

Conservative

Font styles to use
Serif

Colors
abd037
85cae6
cadf82
34a7d7
ffffff
886aae
6b449b

Requirements
Must have
• I like zen-like calming effects. lime Green, light blues and purple. I like waves and color.
• I like water and light, flowers and plants - bamboo, stacking rocks, ocean, water, lotus flowers
Should not have
• not too much purple
• Mostly green and blue

```html
<!DOCTYPE html>
<html lang="en">
<head>
<meta charset="utf-8">
<title>Gentle Horizon Therapy – Trifold</title>
<link href="https://fonts.googleapis.com/css2?family=Raleway:wght@300;400;500;600;700&family=Bree+Serif&family=Pinyon+Script&display=swap" rel="stylesheet">
<style>
:root{
  --lime:#abd037;
  --lime-soft:#cadf82;
  --sky:#85cae6;
  --blue:#34a7d7;
  --blue-deep:#1c5f9c;
  --navy:#1d3f7a;
  --purple:#6b449b;
  --lavender:#886aae;
  --white:#ffffff;
  --ink:#4a4a4a;
  --grey:#7a7a7a;
  --page:#dedede;
  --olive:#4d7a1f;
}
*{margin:0;padding:0;box-sizing:border-box}
html,body{width:757px;height:1200px;overflow:hidden;background:var(--page)}
body{position:relative;font-family:"Raleway",Arial,sans-serif;color:var(--ink)}
.spread{position:absolute;left:50px;width:658px;height:507px;background:var(--white);overflow:hidden;box-shadow:0 6px 14px rgba(0,0,0,.25)}
.spread--outside{top:60px}
.spread--inside{top:626px;height:505px}
.layer{position:absolute;inset:0}
.abs{position:absolute}
.placeholder{position:absolute}

/* outside: services panel */
.services{left:14px;top:14px;width:190px}
.services__title{font-size:18px;line-height:19px;font-weight:600;color:var(--lime)}
.services__title span{display:block;font-weight:400}
.services__rule{height:1px;background:var(--lime-soft);margin:6px 0 8px}
.service__label{display:inline-block;background:var(--lime);color:var(--white);font-size:7.6px;font-weight:600;padding:1px 4px 1px 12px;margin-left:-14px;margin-top:9px}
.service__text{font-size:7.5px;line-height:9.6px;color:var(--grey);text-align:justify;margin-top:5px}
.fee{left:14px;top:470px;width:200px;font-size:7.8px;line-height:9.5px;color:var(--white);font-weight:500}

/* outside: contact panel */
.contact{left:220px;width:219px;top:0;text-align:center}
.brand__mark{width:34px;height:34px;border-radius:50%;background:var(--lime);margin:26px auto 8px}
.brand__name{font-size:12.5px;letter-spacing:3px;font-weight:500;color:#3d3d3d;line-height:14px}
.brand__sub{font-size:7.5px;letter-spacing:1.4px;font-weight:500;color:#3d3d3d}
.contact__doctor{margin-top:24px;font-size:9.6px;line-height:11.5px;font-weight:500;color:var(--navy)}
.contact__motto{margin-top:6px;font-size:7.8px;line-height:9.8px;color:var(--navy)}
.contact__pin{margin:5px auto 0;display:block}
.contact__label{font-size:9.2px;color:var(--navy);font-weight:500}
.contact__address{font-size:7.6px;line-height:9.6px;color:var(--ink)}
.contact__phone{margin-top:20px;font-size:20px;font-weight:700;color:var(--blue-deep);display:flex;align-items:center;justify-content:center;gap:5px}
.web-pill{position:absolute;top:488px;width:134px;height:14px;border-radius:8px;background:var(--lime);font-size:8.8px;line-height:14px;text-align:center;color:var(--navy);font-weight:500}

/* outside: cover panel */
.cover{left:439px;width:219px;text-align:center;color:var(--white)}
.cover__title{top:180px}
.script{font-family:"Pinyon Script",cursive;font-size:34px;line-height:34px;text-shadow:0 1px 3px rgba(0,0,0,.35)}
.script--small{font-size:30px;line-height:30px}
.cover__plain{font-size:17px;line-height:19px;font-weight:400;text-shadow:0 1px 3px rgba(0,0,0,.35)}
.cover__info{top:378px}
.cover__name{font-family:"Bree Serif",Georgia,serif;font-size:13.5px;line-height:16px}
.cover__tagline{font-family:"Bree Serif",Georgia,serif;font-size:19px;margin:2px 14px 0;border-top:1px solid var(--white);padding-top:1px;line-height:22px}
.cover__role{font-size:12.5px;line-height:15px;font-weight:400;margin:0 14px;border-bottom:1px solid var(--white);padding-bottom:2px}
.cover__special{margin-top:4px;font-size:12px;line-height:13px;font-weight:400}
.cover__special b{font-weight:700}
.cover__phone{font-size:15px;line-height:17px;margin-top:2px;font-weight:500;letter-spacing:.5px}

/* inside: about therapy panel */
.about{left:14px;top:22px;width:192px;color:var(--white)}
.about__q{font-size:19px;line-height:19px;font-weight:700}
.about__name{font-size:14px;line-height:16px;font-weight:500;color:var(--lime)}
.about__acr{font-size:19px;line-height:20px;font-weight:600;color:var(--lime)}
.about__text{margin-top:8px;width:172px;font-size:7.5px;line-height:9.7px;text-align:justify}
.effective{left:60px;top:300px;width:143px;text-align:right;font-size:13.5px;line-height:16px;font-weight:500;color:var(--navy)}
.problems{left:20px;top:412px;width:190px;list-style:none;font-size:7.6px;line-height:9.6px;color:var(--white)}
.problems li::before{content:"• "}

/* inside: middle panel */
.story{left:231px;top:20px;width:192px}
.story__title{font-size:10.2px;line-height:12.5px;font-weight:700;color:var(--navy);letter-spacing:.2px}
.story__text{margin-top:6px;font-size:7.4px;line-height:9.2px;color:var(--grey);text-align:justify}
.story__bar{margin-top:7px;background:var(--purple);color:var(--white);font-size:8.6px;font-weight:600;padding:2px 6px;display:inline-block;width:174px}
.story__list{list-style:none;margin-top:4px;text-align:right;font-size:6.8px;line-height:8.1px;color:var(--grey)}
.story__list li::before{content:"• "}

/* inside: bio panel */
.portrait{left:490px;top:30px;width:110px;height:110px;border-radius:50%;border:4px solid var(--white);background:radial-gradient(circle at 50% 40%,#e8c8a8,#bf8f6a 55%,#9fc7d9 100%);box-shadow:0 1px 4px rgba(0,0,0,.25)}
.bio{left:446px;top:182px;width:198px}
.bio__name{font-size:18px;font-weight:500;color:var(--olive);text-align:center}
.bio__text{margin-top:8px;font-size:7.5px;line-height:9.5px;color:#3b4a1e;text-align:justify}
</style>
</head>
<body>

<!-- OUTSIDE SPREAD -->
<section class="spread spread--outside">
  <div class="placeholder" role="img" aria-label="Calm ocean water surface photo" style="left:220px;top:190px;width:219px;height:317px;background:linear-gradient(180deg,rgba(255,255,255,1) 0%,#cdebef 18%,#7fc7d4 45%,#3f97b8 75%,#2b7fa8 100%)"></div>
  <div class="placeholder" role="img" aria-label="Close-up photo of a purple lotus flower" style="left:439px;top:0;width:219px;height:400px;background:radial-gradient(ellipse at 60% 30%,#b48fe0 0%,#7b58b8 35%,#3f4a3a 75%,#1f3122 100%)"></div>

  <svg class="layer" width="658" height="507" viewBox="0 0 658 507" aria-hidden="true">
    <defs>
      <linearGradient id="band1" x1="0" y1="0" x2="1" y2="0">
        <stop offset="0" stop-color="#1d5f9a"/>
        <stop offset=".55" stop-color="#2a8cc6"/>
        <stop offset="1" stop-color="#34a7d7"/>
      </linearGradient>
    </defs>
    <path d="M0,400 C120,395 220,440 300,430 C360,420 420,330 658,280 L658,507 L0,507Z" fill="var(--lime)"/>
    <path d="M0,412 C120,407 220,452 300,442 C360,432 420,342 658,292 L658,507 L0,507Z" fill="var(--white)"/>
    <path d="M0,422 C120,417 220,462 300,452 C360,442 420,352 658,302 L658,507 L0,507Z" fill="url(#band1)"/>
    <line x1="220" y1="0" x2="220" y2="507" stroke="rgba(0,0,0,.06)"/>
    <line x1="439" y1="0" x2="439" y2="507" stroke="rgba(0,0,0,.06)"/>
  </svg>

  <div class="abs services">
    <h2 class="services__title">Psychological<span>Services</span></h2>
    <div class="services__rule"></div>
    <div class="service">
      <div class="service__label">Initial evaluation</div>
      <p class="service__text">Mental health assessment, diagnosis and comprehensive wellness planning.</p>
    </div>
    <div class="service">
      <div class="service__label">Gentle Horizon Therapy (GHT)</div>
      <p class="service__text">Resolve emotional distress, heartbreak and grief. GHT clears trauma at the subconscious level with hypnotic communication. The most troubling of memories are worked through and clients gain a sense of clarity, peace and power. Only a couple of sessions are needed to experience dramatic and long-lasting effects.</p>
    </div>
    <div class="service">
      <div class="service__label">Eye Movement Desensitization and Reprocessing (EMDR)</div>
      <p class="service__text">Evidence-based treatment for post-traumatic stress disorder, anxiety, depression and adverse experiences. Experience relief and empowerment. More information at traumarelief.org.</p>
    </div>
    <div class="service">
      <div class="service__label">Short-term talk therapy</div>
      <p class="service__text">Psychotherapy to create a more satisfying life. Proactive approach to seeking effective solutions for your most pressing emotional and relational problems.</p>
    </div>
    <div class="service">
      <div class="service__label">Meditation for Wellness</div>
      <p class="service__text">Personalized meditation for calm, healing and well-being.</p>
    </div>
  </div>
  <p class="abs fee">Fee Information: ShoreCare and FleetCare accepted and filed.</p>

  <div class="abs contact">
    <div class="brand__mark"></div>
    <div class="brand__name">STILLWATER</div>
    <div class="brand__sub">holistic wellness center</div>
    <p class="contact__doctor">Marianne Dobbs, Psy.D.<br>Licensed Psychologist</p>
    <p class="contact__motto">· Heal the Past<br>· Embrace the Present<br>· Create the Future</p>
    <svg class="contact__pin" width="9" height="12" viewBox="0 0 9 12" aria-hidden="true"><path d="M4.5,0 C2,0 0,2 0,4.5 C0,7.5 4.5,12 4.5,12 C4.5,12 9,7.5 9,4.5 C9,2 7,0 4.5,0Z" fill="var(--lime)"/><circle cx="4.5" cy="4.5" r="1.7" fill="#fff"/></svg>
    <p class="contact__label">Office Location:</p>
    <p class="contact__address">Harbor Plaza<br>2210 Coastline Rd #18<br>Seabrook, FL &nbsp;32900</p>
    <p class="contact__phone"><svg width="16" height="16" viewBox="0 0 24 24" aria-hidden="true"><path d="M6.6 10.8c1.4 2.8 3.8 5.1 6.6 6.6l2.2-2.2c.3-.3.7-.4 1-.2 1.1.4 2.3.6 3.6.6.6 0 1 .4 1 1V20c0 .6-.4 1-1 1C10.6 21 3 13.4 3 4c0-.6.4-1 1-1h3.5c.6 0 1 .4 1 1 0 1.3.2 2.5.6 3.6.1.3 0 .7-.2 1L6.6 10.8z" fill="var(--blue-deep)"/></svg>555 014-2276</p>
  </div>
  <div class="web-pill" style="left:262px">www.stillwaterhwc.com</div>

  <div class="abs cover cover__title">
    <div class="script">Unleashing</div>
    <div class="cover__plain">the Power of the</div>
    <div class="script script--small">Mind for Healing</div>
    <div class="cover__plain">and Well-being</div>
  </div>
  <div class="abs cover cover__info">
    <div class="cover__name">Marianne Dobbs, Psy.D.</div>
    <div class="cover__tagline">Live Well, Love Well</div>
    <div class="cover__role">Licensed Psychologist</div>
    <div class="cover__special">Specializing in <b>Adults</b> and<br><b>Gentle Horizon Therapy</b></div>
    <div class="cover__phone">555 014-2276</div>
  </div>
  <div class="web-pill" style="left:481px">www.stillwaterhwc.com</div>
</section>

<!-- INSIDE SPREAD -->
<section class="spread spread--inside">
  <div class="placeholder" role="img" aria-label="Green meadow photo with a dandelion seed head" style="left:436px;top:0;width:217px;height:505px;background:linear-gradient(180deg,#a9cd45 0%,#9cc43a 55%,#7fae2a 78%,#5f8f22 100%)"></div>

  <svg class="layer" width="653" height="505" viewBox="0 0 653 505" aria-hidden="true">
    <defs>
      <linearGradient id="band2" x1="0" y1="0" x2="1" y2="0">
        <stop offset="0" stop-color="#2a8cc6"/>
        <stop offset=".6" stop-color="#1d64a3"/>
        <stop offset="1" stop-color="#1a5a98"/>
      </linearGradient>
      <linearGradient id="topblue" x1="0" y1="0" x2="0" y2="1">
        <stop offset="0" stop-color="#1d66a8"/>
        <stop offset="1" stop-color="#2f9bd2"/>
      </linearGradient>
    </defs>
    <path d="M0,0 L200,0 C225,90 225,190 160,245 C105,290 45,310 0,325Z" fill="url(#topblue)"/>
    <path d="M208,0 C233,90 233,195 168,252 C113,298 50,320 0,335" fill="none" stroke="var(--lime)" stroke-width="5"/>
    <path d="M218,0 C243,95 242,202 176,260 C120,306 56,330 0,345" fill="none" stroke="var(--lime-soft)" stroke-width="2"/>
    <path d="M0,370 C90,362 180,372 260,396 C330,445 500,465 653,435 L653,505 L0,505Z" fill="var(--lime)"/>
    <path d="M0,380 C90,372 180,382 260,406 C330,455 500,475 653,445 L653,505 L0,505Z" fill="var(--white)"/>
    <path d="M0,388 C90,380 180,390 260,414 C330,463 500,483 653,453 L653,505 L0,505Z" fill="url(#band2)"/>
    <line x1="217" y1="0" x2="217" y2="505" stroke="rgba(0,0,0,.06)"/>
  </svg>

  <div class="abs about">
    <div class="about__q">What is</div>
    <div class="about__name">Gentle Horizon Therapy</div>
    <div class="about__acr">(GHT)</div>
    <p class="about__text">GHT dramatically enhances mood, creates calm, eases grief, optimizes health and promotes success. It is a form of hypnosis that clears stuck patterns of thinking and feeling at the subconscious level. Past emotionally charged memories are cleared. You do not have to talk about problems, share scattered thoughts, cry nor re-experience uncomfortable emotions. You are guided to engage in deep brain processing to create an internal shift for automatic changes in thoughts, feelings and behaviors. Profound change happens within your nervous system facilitating lasting positive effects. Only one or two sessions are needed to experience immediate symptom relief.</p>
  </div>
  <p class="abs effective">GHT is effective for many of life’s problems including:</p>
  <ul class="abs problems">
    <li>PTSD, Sexual Abuse and Childhood Abuse</li>
    <li>Grief, Infidelity and Heartbreak</li>
    <li>Relationship issues</li>
    <li>Anger and Resentment</li>
    <li>Guilt / Shame</li>
    <li>Anxiety / Fear</li>
    <li>Nightmares / Insomnia</li>
    <li>Stress-related symptoms and Pain</li>
  </ul>

  <div class="abs story">
    <h3 class="story__title">CLEARING OLD STUFF AND MAKING WAY FOR NEW BEGINNINGS</h3>
    <p class="story__text">If you have been unable to change how you feel, think or act, it is likely that you are being affected by experiences from your past. When something is painful or disturbing, it slams into awareness and leaves a lasting impression. Even when the experience is finished, deeper parts of the mind may continue to respond as if the disturbing event is still occurring. When fueled by the ongoing influence of past events, emotional problems, destructive behaviors and relationship difficulties are impossible to overcome. You may consciously understand the value of changing a behavior, but unless your deeper mind is transformed, change is not likely. In GHT the subconscious mind is engaged, and the influence of past events is eliminated. Energy that was blocked is released and healing takes place. Negative habits and painful emotions are replaced by feelings of well-being and motivation for desired action.</p>
    <div class="story__bar">What happens in a GHT Session?</div>
    <p class="story__text">Trauma is stored in the mind and body. In GHT, you will experience profound physiological calm and you will be guided towards emotional resolution in a gentle, creative and even humorous way. You access inner resources of light, wisdom and peace. You step into the awareness of your wise and true self. As Jonah Hale states: “we all have a beautiful light within, we just sometimes forget it is there”. From this place of light, emotional memories are easily reframed with new meaning. You will leave the session feeling peaceful and sourced from within by a free-flowing energy.</p>
    <div class="story__bar">Clear Your Mind and Change Your World</div>
    <ul class="story__list">
      <li>Discover and resolve subconscious causes<br>for emotional and behavioral difficulties</li>
      <li>Eliminate unconscious conflicts blocking<br>desired change</li>
      <li>Promote mind / body healing</li>
    </ul>
  </div>

  <div class="abs portrait" role="img" aria-label="Portrait photo of Dr. Marianne Dobbs"></div>
  <div class="abs bio">
    <h3 class="bio__name">Dr. Marianne Dobbs</h3>
    <p class="bio__text">Dr. Dobbs is a licensed clinical psychologist specializing in adults and seniors. She treats people for depression, anxiety, grief, sexual trauma, PTSD, relationship issues, infidelity, divorce and stress-related symptoms. She has over 20 years of clinical experience in mental health and is an adjunct counseling professor at Bayfield University. She received her Master’s and Doctorate degrees in Clinical Psychology from Kona Pacific University in Honolulu, Hawaii. She earned a Bachelor’s of Science degree in Rehabilitation Medicine from Lakeshore University in Kingston, Canada. At Stillwater Holistic Wellness Center, she provides initial evaluations, assessment, diagnosis and comprehensive treatment planning. She will collaborate with you to create solutions for healing, empowerment and wellness.</p>
  </div>
</section>

</body>
</html>
```